Business Card Design Project

Use our current logo. Clean design.

Industry/Entity Type

Business

Requirements
Must have
• Marisela DUBRANCQ
M. Law
Managing Partner

Alpenvorsa AG
Kornhalmweg 214
CH-3097 Liebefeld

M. +41 79 412 56 27
T. +41 31 928 44 10
F. +41 31 928 44 19

m.dubrancq@alpenvorsa-example.com
www.alpenvorsa-example.com

```html
<!DOCTYPE html>
<html lang="en">
<head>
<meta charset="utf-8">
<title>Alpenvorsa AG – Business Card</title>
<link rel="stylesheet" href="https://fonts.googleapis.com/css2?family=Marcellus&family=Oswald:wght@400;600&family=Open+Sans:wght@400;600&display=swap">
<style>
  :root {
    --stage: #2b2b2d;
    --brand-red: #e2474d;
    --ribbon-red: #d8262c;
    --ribbon-shade: #8e1418;
    --card-dark: #1e1e20;
    --card-dark-2: #2c2c2f;
    --card-light: #ffffff;
    --card-light-edge: #e9e9ea;
    --label-grey: #b9b9bc;
    --accent-orange: #f6a04a;
    --white: #ffffff;
  }
  * { box-sizing: border-box; margin: 0; padding: 0; }
  html, body { width: 1200px; height: 800px; overflow: hidden; }
  body {
    background: var(--stage);
    display: flex;
    align-items: center;
    justify-content: center;
    gap: 44px;
  }
  .card {
    position: relative;
    width: 540px;
    height: 330px;
    border: 16px solid var(--brand-red);
    overflow: hidden;
  }

  /* Back side */
  .card--back {
    background: linear-gradient(135deg, var(--card-dark-2) 0%, var(--card-dark) 60%, #161618 100%);
  }
  .card--back .ribbon {
    position: absolute;
    inset: 0;
    width: 100%;
    height: 100%;
  }
  .identity {
    position: absolute;
    left: 212px;
    top: 36px;
  }
  .identity__name {
    font-family: "Oswald", sans-serif;
    font-weight: 600;
    font-size: 19px;
    letter-spacing: 0.5px;
    color: var(--white);
    text-transform: uppercase;
  }
  .identity__title {
    font-family: "Open Sans", sans-serif;
    font-size: 11px;
    color: var(--accent-orange);
    margin-top: 1px;
  }
  .contact-list {
    position: absolute;
    left: 38px;
    top: 150px;
    font-family: "Open Sans", sans-serif;
    font-size: 11px;
    color: var(--label-grey);
    line-height: 20px;
    display: grid;
    grid-template-columns: 72px auto;
  }
  .contact-list dd { color: var(--white); }
  .address {
    position: absolute;
    right: 30px;
    top: 150px;
    font-family: "Open Sans", sans-serif;
    font-style: normal;
    font-size: 11px;
    line-height: 20px;
    color: var(--brand-red);
  }
  .address__online {
    display: block;
    margin-top: 14px;
    color: var(--white);
  }

  /* Front side */
  .card--front {
    background: radial-gradient(ellipse at center, var(--card-light) 40%, var(--card-light-edge) 100%);
    display: flex;
    align-items: center;
    justify-content: center;
  }
  .wordmark {
    font-family: "Marcellus", serif;
    font-weight: 400;
    font-size: 44px;
    letter-spacing: 2px;
    color: var(--brand-red);
    text-transform: uppercase;
  }
</style>
</head>
<body>

  <section class="card card--back" aria-label="Card back with contact details">
    <svg class="ribbon" viewBox="0 0 508 298" preserveAspectRatio="none" aria-hidden="true">
      <polygon points="150,60 195,22 195,84 150,122" fill="var(--ribbon-shade)"/>
      <polygon points="0,122 150,60 150,122 0,184" fill="#b31c21" opacity="0.55"/>
      <polygon points="195,22 508,22 508,84 195,84" fill="var(--ribbon-red)"/>
    </svg>
    <div class="identity">
      <p class="identity__name">Marisela Dubrancq</p>
      <p class="identity__title">M. Law · Managing Partner</p>
    </div>
    <dl class="contact-list">
      <dt>Mobile</dt><dd>: +41 79 412 56 27</dd>
      <dt>Telephone</dt><dd>: +41 31 928 44 10</dd>
      <dt>Fax</dt><dd>: +41 31 928 44 19</dd>
    </dl>
    <address class="address">
      Alpenvorsa AG<br>
      Kornhalmweg 214<br>
      CH-3097 Liebefeld
      <span class="address__online">
        m.dubrancq@alpenvorsa-example.com<br>
        www.alpenvorsa-example.com
      </span>
    </address>
  </section>

  <section class="card card--front" aria-label="Card front">
    <p class="wordmark">Alpenvorsa</p>
  </section>

</body>
</html>
```